Promotional brochure for educational consulting firm

Hi Designers!

Please do a 8.5 x 11 inch tri-fold brochure as well as a 8.5 x 11 inch half-fold brochure.  I appreciate black and white versions in addition to color.  Please take a look at my company's website for a better sense of the look and feel I am going for:  www.brightlarkedu.org

Thanks!

Industry/Entity Type

Consulting

Colors
3176b5
85abd2
fcfbfd

```html
<!DOCTYPE html>
<html lang="en">
<head>
<meta charset="utf-8">
<title>Brightlark Associates – Tri-fold Brochure</title>
<link rel="stylesheet" href="https://fonts.googleapis.com/css2?family=Open+Sans:wght@400;600;700&family=Tinos:wght@400;700&display=swap">
<style>
:root{
  --board:#d3aa66;
  --board-edge:#e2c48f;
  --blue:#0058a8;
  --blue-soft:#7d99c4;
  --grey:#b8babd;
  --paper:#ffffff;
  --ink:#3c3c3c;
  --ink-soft:#555;
}
*{margin:0;padding:0;box-sizing:border-box}
html,body{width:1200px;height:1001px;overflow:hidden}
body{background:var(--board);font-family:"Open Sans",Arial,sans-serif;color:var(--ink);position:relative}
.board-edge{position:absolute;left:4px;top:4px;width:1200px;height:1001px;border:2px solid var(--board-edge);pointer-events:none}
.spread{position:absolute;background:var(--paper);overflow:hidden}
.outside{left:307px;top:33px;width:595px;height:459px}
.inside{left:307px;top:522px;width:585px;height:453px}
.block{position:absolute}
.blue{background:var(--blue)}
.grey{background:var(--grey)}
.contact{position:absolute;left:0;top:162px;width:198px;text-align:center;font-size:8px;line-height:10.5px;color:#222}
.contact h3{font-size:8px;font-weight:600;margin-bottom:10px}
.brand{display:flex;align-items:center;justify-content:center;gap:5px;color:var(--blue);font-weight:700;text-transform:uppercase;letter-spacing:.3px}
.brand .dot{width:10px;height:10px;border-radius:50%;background:var(--blue);flex:none}
.brand-small{font-size:7px;margin-top:30px}
.brand-large{position:absolute;left:396px;top:245px;width:199px;font-size:9px}
.tagline{position:absolute;left:198px;top:213px;width:198px;text-align:center;font-family:"Tinos","Times New Roman",serif;font-size:14px;line-height:16px;color:#111}
.tagline strong{color:var(--blue);font-size:14.5px}
.mark-circle{position:absolute;left:76px;top:57px;width:44px;height:44px;border-radius:50%;border:6px solid var(--blue-soft)}
.intro{position:absolute;left:29px;top:126px;width:141px;font-size:7.2px;line-height:10.8px;text-align:justify;color:var(--ink-soft)}
.intro p+p{margin-top:10px}
.intro .name{color:var(--blue)}
.art{position:absolute}
.questions{position:absolute;left:215px;top:161px;width:162px;font-size:6.6px;line-height:9.8px;color:var(--blue);list-style:none}
.questions li{margin-bottom:10px}
.photo{position:absolute;left:453px;top:45px;width:69px;height:89px;border:2px solid #999;background:linear-gradient(180deg,#9c9c9c,#5e5e5e)}
.person{position:absolute;left:417px;top:137px;width:142px;text-align:center}
.person h2{font-size:8.5px;font-weight:700;color:var(--blue)}
.person p{font-size:6.5px;font-style:italic;color:#333;margin-top:2px}
.bio{position:absolute;left:418px;top:179px;width:140px;font-size:6.7px;line-height:9.8px;text-align:justify;color:var(--ink-soft)}
.bio strong{color:var(--blue)}
.expertise{position:absolute;left:418px;top:276px;width:160px}
.expertise h3{font-size:9.5px;font-weight:700;color:var(--blue);margin-bottom:7px}
.expertise ul{list-style:none;font-size:6.8px;color:var(--ink-soft)}
.expertise li{display:flex;align-items:center;gap:5px;height:14.4px}
.expertise li::before{content:"";width:8px;height:8px;border-radius:50%;border:1.5px solid var(--blue);flex:none}
</style>
</head>
<body>
<div class="board-edge"></div>

<section class="spread outside" aria-label="Brochure outside">
  <div class="block blue" style="left:0;top:0;width:198px;height:144px"></div>
  <div class="block grey" style="left:0;top:315px;width:198px;height:144px"></div>
  <div class="contact">
    <h3>Contact Us</h3>
    <p>Marisol Teng, Ed.D.</p>
    <p>[t]&nbsp; 555.014.2280</p>
    <p>[f]&nbsp; 555.014.7731</p>
    <p>marisol@brightlarkedu.org</p>
    <p>www.brightlarkedu.org</p>
    <div class="brand brand-small"><span class="dot"></span>Brightlark Associates LLC</div>
  </div>
  <div class="tagline">School leadership is<br><strong>24/7/365</strong></div>
  <div class="block grey" style="left:396px;top:0;width:199px;height:173px"></div>
  <div class="brand brand-large"><span class="dot"></span>Brightlark Associates LLC</div>
  <div class="block blue" style="left:396px;top:287px;width:199px;height:172px"></div>
</section>

<section class="spread inside" aria-label="Brochure inside">
  <div class="block grey" style="left:0;top:0;width:195px;height:23px"></div>
  <div class="block blue" style="left:195px;top:0;width:195px;height:23px"></div>
  <div class="block grey" style="left:390px;top:0;width:195px;height:23px"></div>

  <div class="mark-circle"></div>
  <div class="intro">
    <p><span class="name">Brightlark Associates</span> provides just-in-time support to schools and school leaders.</p>
    <p>Schools along the continuum of organizational growth from startup schools to developing or mature schools can benefit from specialized expertise to complete a time-sensitive special project or develop strategies and processes to take their program to the next level of excellence.</p>
  </div>
  <div class="art" role="img" aria-label="Illustration of figures lifting a rising green growth arrow" style="left:0;top:283px;width:140px;height:127px;background:linear-gradient(135deg,#8fd14f 0%,#f2d23a 55%,#e8e8e8 80%,#ffffff 100%)"></div>

  <div class="art" role="img" aria-label="Illustration of a figure standing beside a question mark sign" style="left:255px;top:58px;width:85px;height:80px;background:linear-gradient(135deg,#cfe6f7,#f1f1f1)"></div>
  <ul class="questions">
    <li>How do I develop a high-functioning board?</li>
    <li>What policies do start-up schools need to have on day one?</li>
    <li>Is my meal program optimizing revenue?</li>
    <li>We want to refinance our property. How do we tell our story to a lender?</li>
    <li>How can we increase parent engagement?</li>
    <li>What do we need to do to increase visibility (and enrollment)?</li>
    <li>My assistant principal is going out on extended leave... can I get someone to step in while he's out?</li>
    <li>Do these questions keep you up at night? If so, we can help.</li>
  </ul>

  <div class="photo" role="img" aria-label="Portrait photograph of the founder"></div>
  <div class="person">
    <h2>Marisol Teng, Ed.D.</h2>
    <p>Founder &amp; CEO</p>
  </div>
  <p class="bio">My 10-year experience as an executive director of charter schools in the two largest school districts in California gives me a unique <strong>“education + business”</strong> perspective in addition to a network of on-call, expert associates who are ready to assist your school in a variety of key areas.</p>
  <div class="expertise">
    <h3>Our areas of expertise include:</h3>
    <ul>
      <li>Board Training</li>
      <li>Budget and Operations</li>
      <li>Charter Development</li>
      <li>Communications</li>
      <li>Leadership Coaching</li>
      <li>Lender Negotiations</li>
      <li>Fund Development</li>
      <li>Placement of interim administrators</li>
    </ul>
  </div>

  <div class="block blue" style="left:0;top:432px;width:195px;height:21px"></div>
  <div class="block grey" style="left:195px;top:432px;width:195px;height:21px"></div>
  <div class="block blue" style="left:390px;top:432px;width:195px;height:21px"></div>
</section>
</body>
</html>
```